A start up Private Wine Label for export to Asia.

We are looking for the best graphic design for our very first wine label Corvessa Vineyards and would like the following requirements:

1. Black background - explore and play around the shade of black
2. Gold Shimmery Colour Font
3. Font should be a cursive classic posh that says Corvessa Vineyards
4. We would like the front graphic design to be simple and elegant and has a traditional classic feel to it.

Target Market(s)

Small scale to test the upper class market for export to Asia

Font styles to use
Script

Colors

Designer to choose colors to be used in the design.

Requirements
Must have
• Gold font for the label Corvessa Vineyards with shimmery touch to it.
• Elegant black background.
• Simple but elegant design.
• Attractive to the upper class market in Asia.
Nice to have
• Explore and play around with your imagination.

```html
<!DOCTYPE html>
<html lang="en">
<head>
<meta charset="utf-8">
<title>Corvessa Vineyards – Wine Label</title>
<link rel="stylesheet" href="https://fonts.googleapis.com/css2?family=Pinyon+Script&display=swap">
<style>
  :root {
    --canvas-bg: #f3efee;
    --label-black: #1b1c1b;
    --pattern-tone: #222423;
    --gold-deep: #8a6a1e;
    --gold-mid: #c49a3a;
    --gold-light: #f6e08e;
    --gold-line: #b8913a;
  }
  * { margin: 0; padding: 0; box-sizing: border-box; }
  html, body {
    width: 1200px;
    height: 960px;
    overflow: hidden;
    background: var(--canvas-bg);
  }
  .canvas {
    position: relative;
    width: 1200px;
    height: 960px;
  }
  .wine-label {
    position: absolute;
    left: 300px;
    top: 70px;
    width: 600px;
    height: 820px;
    background: var(--label-black);
    box-shadow: 0 8px 30px rgba(0,0,0,0.18);
  }
  .label-frame {
    position: absolute;
    left: 8px;
    right: 8px;
    top: 127px;
    height: 545px;
    border-left: 1.5px solid var(--gold-line);
    border-right: 1.5px solid var(--gold-line);
  }
  .frame-rule {
    position: absolute;
    left: 0;
    right: 0;
    height: 2px;
    background: linear-gradient(90deg, var(--gold-deep), var(--gold-light) 50%, var(--gold-deep));
  }
  .frame-rule.top { top: 127px; }
  .frame-rule.bottom { top: 672px; }
  .pattern-field {
    position: absolute;
    inset: 0;
    background: var(--pattern-tone);
  }
  .brand {
    position: absolute;
    left: 0;
    right: 0;
    text-align: center;
    font-family: "Pinyon Script", cursive;
    font-weight: 400;
    background: linear-gradient(180deg, var(--gold-light) 0%, var(--gold-mid) 45%, var(--gold-deep) 60%, var(--gold-light) 100%);
    -webkit-background-clip: text;
    background-clip: text;
    color: transparent;
    line-height: 1;
  }
  .brand-name {
    top: 300px;
    font-size: 120px;
  }
  .brand-sub {
    top: 445px;
    font-size: 64px;
  }
</style>
</head>
<body>
  <main class="canvas">
    <section class="wine-label">
      <div class="label-frame">
        <div class="pattern-field" role="img" aria-label="Faint dark grey geometric line pattern"></div>
      </div>
      <div class="frame-rule top"></div>
      <div class="frame-rule bottom"></div>
      <h1 class="brand brand-name">Corvessa</h1>
      <p class="brand brand-sub">Vineyards</p>
    </section>
  </main>
</body>
</html>
```